Quill And Ferry Business Card

I need a business card designed around my logo (which was designed here on Sketch Forum!)

Target Market(s)

Professional Businesses

Industry/Entity Type

Business

Requirements
Must have
• Details that must be on the business card:

Renata Ovalle
Director
0491 253 608
renata@quillandferry.com.au
www.quillandferry.com.au
PO Box 4720 Larkspur Vale Vic 3994

```html
<!DOCTYPE html>
<html lang="en">
<head>
<meta charset="utf-8">
<title>Quill And Ferry Business Card</title>
<link rel="stylesheet" href="https://fonts.googleapis.com/css2?family=Cinzel:wght@400&family=Open+Sans:wght@400;700&display=swap">
<style>
  :root {
    --backdrop: #e4e2df;
    --card-light: #ececec;
    --card-dark: #232323;
    --brand-red: #b4142a;
    --brand-grey: #8c8c8c;
    --text-mid: #6a6a6a;
    --text-light: #f2f2f2;
    --shadow: rgba(0, 0, 0, 0.18);
  }
  * { margin: 0; padding: 0; box-sizing: border-box; }
  html, body {
    width: 1200px; height: 900px; overflow: hidden;
    background: var(--backdrop);
  }
  .canvas { position: relative; width: 1200px; height: 900px; }
  .card {
    position: absolute; width: 560px; height: 320px;
    background: var(--card-light);
    box-shadow: 0 6px 18px var(--shadow);
    overflow: hidden;
  }
  .card--front { left: 90px; top: 90px; }
  .card--back { left: 550px; top: 490px; }

  .wordmark {
    font-family: "Cinzel", serif; font-weight: 400;
    color: var(--brand-grey); letter-spacing: 0.02em;
    text-transform: uppercase; line-height: 1; white-space: nowrap;
  }
  .slogan {
    font-family: "Open Sans", sans-serif; font-weight: 400;
    color: var(--text-mid); text-transform: uppercase;
    letter-spacing: 0.18em; line-height: 1; white-space: nowrap;
  }

  /* front */
  .front__square {
    position: absolute; left: 0; top: 80px;
    width: 160px; height: 160px;
    background: var(--brand-red);
  }
  .front__lockup {
    position: absolute; right: 40px; top: 116px; text-align: right;
  }
  .front__lockup .wordmark { font-size: 34px; }
  .front__lockup .slogan { font-size: 12px; margin-top: 10px; }
  .front__url {
    font-family: "Open Sans", sans-serif; font-size: 14px;
    color: var(--brand-grey); letter-spacing: 0.32em; margin-top: 12px;
    white-space: nowrap;
  }

  /* back */
  .back__mark {
    position: absolute; left: 40px; top: 58px;
    width: 34px; height: 34px; background: var(--brand-red);
  }
  .back__lockup { position: absolute; left: 92px; top: 52px; }
  .back__lockup .wordmark { font-size: 30px; }
  .back__lockup .slogan { font-size: 11px; margin-top: 8px; }
  .back__rule {
    position: absolute; left: 0; top: 132px; width: 100%; height: 3px;
    background: var(--brand-red);
  }
  .back__panel {
    position: absolute; left: 0; top: 139px; width: 100%; height: 181px;
    background: var(--card-dark);
    padding: 26px 40px 0 92px;
    font-family: "Open Sans", sans-serif; color: var(--text-light);
  }
  .contact__name { font-size: 18px; font-weight: 700; }
  .contact__role { font-size: 13px; font-weight: 400; margin-left: 8px; letter-spacing: 0.04em; }
  .contact__lines { margin-top: 14px; font-size: 13px; line-height: 1.6; white-space: nowrap; }
  .contact__label { margin-right: 4px; }
  .contact__gap { margin-left: 14px; }
  .contact__web { color: var(--brand-red); font-weight: 700; }
</style>
</head>
<body>
<main class="canvas">

  <section class="card card--front" aria-label="Business card front">
    <div class="front__square"></div>
    <div class="front__lockup">
      <div class="wordmark">Quill And Ferry</div>
      <div class="slogan">Ledgers Kept Simple</div>
      <div class="front__url">www.quillandferry.com.au</div>
    </div>
  </section>

  <section class="card card--back" aria-label="Business card back">
    <div class="back__mark"></div>
    <div class="back__lockup">
      <div class="wordmark">Quill And Ferry</div>
      <div class="slogan">Ledgers Kept Simple</div>
    </div>
    <div class="back__rule"></div>
    <div class="back__panel">
      <div>
        <span class="contact__name">Renata Ovalle</span>
        <span class="contact__role">DIRECTOR</span>
      </div>
      <div class="contact__lines">
        <div>
          <span class="contact__label">t</span>0491 253 608
          <span class="contact__gap contact__label">e</span>renata@quillandferry.com.au
        </div>
        <div>PO Box 4720 Larkspur Vale Vic 3994</div>
        <div class="contact__web">www.quillandferry.com.au</div>
      </div>
    </div>
  </section>

</main>
</body>
</html>
```